Poster Needed for Church Conference

I need a poster for a weekend conference at my church. Looking to attract as many people as possible. We are a church in the suburbs of Houston. This is mainly for our own church members but we are opening it up to outside church members.

Please see previous design from last conference and all other graphic work that can (doesn't need to be) included.

Target Market(s)

It's targeted for all people. But our main audience is families. around the age of 30 should be main target.

Industry/Entity Type

Non-Profit

Font styles to use
Serif
Sans Serif

Colors

Designer to choose colors to be used in the design.

Requirements
Must have
• 11x17 design with ability to shrink and blow up. but ideally for 11x17
• Content and wording:
• "Rooted Light Conference: Bridging the gap between generations and passing on our deepest beliefs and values."
• Featuring Dr. Gil Marsden. Author of "The Path of P4"
• Aug 25-26: Friday 8-10 pm, Saturday 4-8 pm
• Cost Adults $15/Children $5: Covers admission to all sessions and workshops, refreshments and Saturday dinner. *kids 5 and under free
• Childcare provided for all sessions. "
• Please use church logo and address on flyer: 4312 Route 19, Missouri City, TX 77988
Nice to have
• Ideally it will be designed so that we can crop a 16:9 pp announcement slide and header for our website.
Should not have
• anything offensive

```html
<!DOCTYPE html>
<html lang="en">
<head>
<meta charset="utf-8">
<title>Rooted Light Conference</title>
<link rel="stylesheet" href="https://fonts.googleapis.com/css2?family=Oswald:wght@300;500;700&family=Roboto+Condensed:wght@500;700&family=Fondamento&family=Yellowtail&display=block">
<style>
  :root {
    --sky-dark: #2b2418;
    --sky-mid: #6b5424;
    --sun-gold: #e9b451;
    --field-green: #3f5a22;
    --deep-green: #1a4419;
    --darkest-green: #163a17;
    --portrait-light: #d9b291;
    --portrait-mid: #a9876a;
    --portrait-shade: #6e5a45;
    --crimson: #e3113f;
    --ink: #1c1408;
    --white: #ffffff;
    --accent-green: #3aa845;
    --rule: rgba(255,255,255,0.3);
  }
  * { margin: 0; padding: 0; box-sizing: border-box; }
  html, body { width: 776px; height: 1200px; overflow: hidden; background: var(--darkest-green); }
  .poster {
    position: relative; width: 776px; height: 1200px; overflow: hidden;
    background: linear-gradient(180deg, var(--deep-green) 0%, var(--darkest-green) 100%);
    font-family: "Roboto Condensed", sans-serif; color: var(--white);
  }
  .hero-scene {
    position: absolute; left: 0; top: 0; width: 776px; height: 920px;
    background:
      radial-gradient(ellipse 340px 240px at 600px 420px, rgba(250,205,110,0.95), rgba(233,180,81,0.4) 55%, transparent 80%),
      linear-gradient(180deg, var(--sky-dark) 0%, var(--sky-mid) 30%, #a07a36 45%, var(--field-green) 62%, #344b1d 80%, var(--deep-green) 100%);
    -webkit-mask-image: linear-gradient(180deg, #000 85%, transparent 100%);
            mask-image: linear-gradient(180deg, #000 85%, transparent 100%);
  }
  .speaker-photo {
    position: absolute; left: 0; top: 30px; width: 380px; height: 700px;
    background:
      radial-gradient(ellipse 150px 230px at 200px 300px, var(--portrait-light) 0%, var(--portrait-mid) 55%, transparent 100%),
      radial-gradient(ellipse 210px 340px at 170px 360px, var(--portrait-shade) 0%, rgba(110,90,69,0.6) 60%, transparent 100%);
    -webkit-mask-image: linear-gradient(180deg, #000 70%, transparent 100%);
            mask-image: linear-gradient(180deg, #000 70%, transparent 100%);
  }
  .event-name {
    position: absolute; top: 182px; left: 382px; width: 380px; text-align: center;
    font-family: "Oswald", sans-serif; font-weight: 500; font-size: 25px;
  }
  .tagline {
    position: absolute; top: 222px; left: 380px; width: 390px; text-align: center;
    font-family: "Fondamento", serif; font-size: 43px; line-height: 52px; color: var(--ink);
  }
  .speaker-name {
    position: absolute; top: 548px; right: 22px; white-space: nowrap;
    font-family: "Yellowtail", cursive; font-weight: 400; font-size: 72px; line-height: 90px; color: var(--crimson);
    text-shadow: 0 0 2px var(--white), 0 0 2px var(--white);
  }
  .book-title {
    position: absolute; top: 640px; right: 37px;
    font-family: "Oswald", sans-serif; font-weight: 500; font-size: 23px; letter-spacing: 1.5px;
  }
  .book-mark {
    position: absolute; left: 290px; top: 773px; width: 196px; height: 73px;
    background: var(--white); display: flex; align-items: center; justify-content: center;
    font-family: "Oswald", sans-serif; font-weight: 700; font-size: 24px; color: var(--accent-green);
  }
  .dates {
    position: absolute; top: 860px; width: 100%; text-align: center;
    font-family: "Oswald", sans-serif; font-weight: 700; font-size: 52px; line-height: 72px;
  }
  .times {
    position: absolute; top: 938px; width: 100%; text-align: center;
    font-family: "Oswald", sans-serif; font-weight: 300; font-size: 27px; line-height: 36px;
  }
  .rule { position: absolute; left: 82px; width: 610px; height: 1px; background: var(--rule); }
  .rule.top { top: 997px; } .rule.bottom { top: 1097px; }
  .cost-tag { position: absolute; left: 109px; top: 1016px; }
  .cost-tag text { font-family: "Oswald", sans-serif; font-weight: 500; font-size: 24px; fill: var(--accent-green); }
  .price { position: absolute; top: 1013px; text-align: center; font-family: "Oswald", sans-serif; }
  .price .amount { display: block; font-weight: 500; font-size: 36px; line-height: 42px; }
  .price .who { display: block; font-size: 21px; line-height: 28px; }
  .price.adult { left: 218px; width: 62px; } .price.child { left: 336px; width: 84px; }
  .divider { position: absolute; top: 1011px; width: 1px; height: 74px; background: var(--white); }
  .divider.one { left: 310px; } .divider.two { left: 442px; }
  .covers {
    position: absolute; left: 461px; top: 1020px; font-family: "Oswald", sans-serif;
    font-weight: 500; font-size: 22px; line-height: 29px;
  }
  .fine-print {
    position: absolute; top: 1112px; width: 100%; text-align: center;
    font-family: "Roboto Condensed", sans-serif; font-weight: 500; font-size: 17px; line-height: 22px;
  }
  .church {
    position: absolute; top: 1165px; width: 100%;
    display: flex; align-items: center; justify-content: center; gap: 8px;
    font-family: "Roboto Condensed", sans-serif; font-weight: 500; font-size: 14px; line-height: 20px;
    color: var(--white);
  }
  .church-dot { width: 10px; height: 10px; border-radius: 50%; background: var(--white); }
  .church-address { opacity: 0.85; }
</style>
</head>
<body>
<div class="poster">
  <div class="hero-scene" role="img" aria-label="Sunset over a green countryside field with hay bales under a glowing golden sky"></div>
  <div class="speaker-photo" role="img" aria-label="Portrait photo of the speaker, Dr. Gil Marsden, blended into the landscape"></div>

  <p class="event-name">Rooted Light Conference</p>
  <p class="tagline">Bridging the gap between generations and passing on our deepest beliefs and values.</p>

  <p class="speaker-name">Dr. Gil Marsden</p>
  <p class="book-title">The Path of P4</p>

  <div class="book-mark">The Path of P4</div>

  <p class="dates">AUGUST 25-26</p>
  <p class="times">FRIDAY 8-10 PM &nbsp;|&nbsp; SATURDAY 4-8 PM</p>

  <div class="rule top"></div>
  <svg class="cost-tag" width="90" height="68" viewBox="0 0 90 68">
    <polygon points="8,0 78,0 90,34 78,68 0,68 10,34" fill="#ffffff"/>
    <text x="45" y="43" text-anchor="middle">COST</text>
  </svg>
  <div class="price adult"><span class="amount">$15</span><span class="who">Adults</span></div>
  <div class="divider one"></div>
  <div class="price child"><span class="amount">$5</span><span class="who">Children</span></div>
  <div class="divider two"></div>
  <p class="covers">Covers admission to all<br>sessions and workshops</p>
  <div class="rule bottom"></div>

  <p class="fine-print">Refreshments and Saturday dinner. *kids 5 and under free<br>Childcare provided for all sessions.</p>

  <div class="church">
    <span class="church-dot"></span>
    <span class="church-name">Cedar Grove Church</span>
    <span class="church-address">&nbsp;4312 Route 19, Missouri City, TX 77988</span>
  </div>
</div>
</body>
</html>
```